A4 Tri-fold Brochure for Sedation Dentist Specialist Dr. Marlon and Sedation Dentistry.

I would like to create an A4 tri-fold brochure for our Dental Sedation Specialist Dr. Marlon Quade. Please carefully select the most suitable highlights from his bio below.

This brochure has two parts. Highlighting what makes Dr. Marlon Quade unique and trustworthy. Include a picture of him (attached). The second part is about sedation dentistry. All you need to know here: http://www.calmchairhub.example/what-is-calm-chair-treatment

Avoid making it too wordy.

Meet Dr. Rowan Elke Marlon Quade, DDS

Inspired to Become a Dentist:
As a child, Dr. Marlon Quade always felt stressed whenever he had to see a dentist. He knew that he wanted to become a dentist to help put patients completely at ease while they experienced quality dental care.

He is passionate about giving patients the healthy, beautiful smiles they deserve. “I find it fulfilling when I can see my patients’ beautiful smiles and how they can finally appreciate the joy of eating with a healthy set of teeth. However, what I love most about my job is the ability to provide a stress-free and comfortable experience at the dentist’s office, particularly for children, through sedation and general anesthesia.”

Educational Achievements:
Before becoming a dentist, Dr. Marlon Quade earned his undergraduate degree at the University of Northern Albury where he received a Bachelor of Medical Science Honor Specialization degree with distinction in biochemistry. He then completed his Doctor of Dental Surgery degree with honors at the University of Kestrelford. While there, he received the Linus Brandt Medal in his class for outstanding achievement in anesthesia. He then pursued his three-year residency as well as a master’s degree in dental anesthesia at the University of Kestrelford.

So he can provide his patients with the latest in dentistry, Dr. Marlon Quade enjoys pursuing additional knowledge, particularly in the areas of dental anesthesia as well as advanced technologies in dentistry. He is currently part of the Molar Horizons study club and has enrolled in the Core Anchor Short- Training Course. He also serves as a clinical instructor at the Pellvar Clinic at the University of Kestrelford.

Association Memberships:
In addition to his academic credentials, Dr. Marlon Quade is a member of several associations:
The Grand Guild of Oral Practitioners of Varnland (GGOPV)
Dental Continental Union of Dental Sedation (CUDS)
Northern Institute of Dental Sedation (NIDS)
Varnland Dental Council (VDC)
Outside the Practice

When he’s not at the practice, Dr. Marlon Quade enjoys spending time with his wife Greta and their two poodles Pippin and Pepper, who are spoiled rotten! “Greta and I love taking our dogs out on hikes and to the dog park on weekends. I also enjoy a wide range of activities from model building and playing the piano to soccer, gym and archery.” He stays fit by working out at the local Brightstride gym, and he likes to walk in Fernhollow Lake Park and Ashcombe Meadow Park.

Dr. Marlon Quade considers himself to be a kid at heart. He is a big fan of superheroes and animated movies. “I get really excited about any upcoming superhero or Lumawell Studioz movies. Till this day, I still collect superhero toy figures.”

He supports the TinyHearts Trust as well as the Varnland League for the Protection of Companion Creatures (LPCC).

Experience outstanding dental care with our highly skilled dentist. Contact us today to schedule an appointment with Dr. Marlon Quade! He speaks English, Cantonese, and Mandarin.

Target Market(s)

Mothers with young kids.

Industry/Entity Type

Dental

Font styles to use
Sans Serif

Requirements
Should not have
• Prices

```html
<!DOCTYPE html>
<html lang="en">
<head>
<meta charset="utf-8">
<title>Calm Chair Hub – Tri-fold Brochure</title>
<link rel="stylesheet" href="https://fonts.googleapis.com/css2?family=Courgette&family=Oswald:wght@300;400&family=Roboto+Condensed:wght@400;700&display=swap">
<style>
  :root {
    --stage: #5a5a5a;
    --navy: #1b4f8f;
    --blue: #1a6cb3;
    --blue-deep: #155a9c;
    --orange: #f3901e;
    --orange-deep: #e57d10;
    --ink: #2b2b2b;
    --white: #ffffff;
    --photo-sky: #cfe3f2;
    --photo-skin: #e9cdb9;
  }
  * { box-sizing: border-box; margin: 0; padding: 0; }
  html, body { width: 1200px; height: 880px; overflow: hidden; }
  body { background: var(--stage); font-family: "Roboto Condensed", sans-serif; position: relative; }

  .brochure { position: absolute; left: 45px; top: 70px; width: 1110px; height: 740px; display: flex; box-shadow: 0 10px 30px rgba(0,0,0,.45); }
  .panel { position: relative; width: 370px; height: 740px; overflow: hidden; }
  .panel-bg { position: absolute; inset: 0; }

  /* Left panel: biography */
  .panel--bio { background: var(--white); }
  .pill-heading { position: absolute; left: 22px; top: 48px; width: 312px; height: 44px; border-radius: 22px; background: var(--orange); box-shadow: 0 4px 6px rgba(0,0,0,.15); color: var(--white); font-family: "Courgette", cursive; font-size: 21px; font-weight: 400; display: flex; align-items: center; justify-content: center; }
  .bio-text { position: absolute; left: 18px; top: 122px; width: 340px; color: var(--ink); font-size: 13.4px; line-height: 22px; text-align: justify; }
  .bio-text p + p { margin-top: 14px; }
  .bio-signature { position: absolute; left: 0; top: 440px; width: 370px; text-align: center; font-family: "Courgette", cursive; font-size: 19px; color: var(--navy); }
  .bio-photo { position: absolute; left: 0; top: 490px; width: 370px; height: 250px; background: linear-gradient(160deg, #eef5fb 0%, var(--photo-sky) 45%, #7fb6e0 100%); }

  /* Middle panel: contact */
  .panel--contact { background: var(--white); }
  .brand-row { position: absolute; left: 0; top: 34px; width: 330px; display: flex; align-items: center; justify-content: center; gap: 12px; }
  .brand-dot { width: 40px; height: 40px; border-radius: 50%; background: var(--blue); }
  .brand-name { font-family: "Oswald", sans-serif; font-weight: 300; font-size: 34px; color: var(--navy); letter-spacing: .5px; }
  .portrait { position: absolute; left: 30px; top: 112px; width: 290px; height: 290px; border-radius: 50%; border: 10px solid var(--orange); background: linear-gradient(180deg, #d8c3b2 0%, var(--photo-skin) 40%, #2a3656 75%); }
  .contact-title { position: absolute; left: 0; top: 438px; width: 370px; text-align: center; font-family: "Courgette", cursive; font-size: 28px; font-weight: 400; color: var(--white); }
  .contact-icons { position: absolute; left: 0; top: 492px; width: 370px; display: flex; justify-content: center; gap: 9px; }
  .contact-icon { width: 36px; height: 36px; border-radius: 50%; background: var(--orange); display: flex; align-items: center; justify-content: center; }
  .contact-details { position: absolute; left: 0; top: 544px; width: 370px; text-align: center; color: var(--white); font-size: 14.5px; line-height: 19px; }
  .contact-details p + p { margin-top: 8px; }
  .url-pill { position: absolute; height: 44px; border-radius: 22px 0 0 22px; background: var(--orange); border: 3px solid var(--white); border-right: none; display: flex; align-items: center; gap: 10px; padding-left: 16px; color: var(--white); font-size: 21px; letter-spacing: .3px; }
  .panel--contact .url-pill { left: 30px; top: 670px; width: 345px; }

  /* Right panel: cover */
  .panel--cover { background: linear-gradient(160deg, #1f78c0 0%, var(--blue) 50%, var(--blue-deep) 100%); }
  .cover-brand { position: absolute; left: 0; top: 60px; width: 370px; display: flex; flex-direction: column; align-items: center; gap: 14px; }
  .cover-brand .brand-dot { width: 70px; height: 70px; background: var(--white); }
  .cover-brand .brand-name { color: var(--white); font-size: 50px; }
  .panel--cover .url-pill { left: 18px; top: 265px; width: 360px; }
  .cover-tagline { position: absolute; left: 36px; top: 350px; color: var(--white); font-family: "Courgette", cursive; font-size: 19px; line-height: 31px; }
  .cover-photo { position: absolute; inset: 0; }
</style>
</head>
<body>
<main class="brochure">

  <section class="panel panel--bio">
    <h2 class="pill-heading">Inspired to Become a Dentist</h2>
    <div class="bio-text">
      <p>As a child, <strong>Dr. Marlon Quade</strong> always felt stressed whenever he had to see a dentist. He knew that he wanted to become a dentist to help put patients completely at ease while they experienced quality dental care.</p>
      <p>He is passionate about giving patients the healthy, beautiful smiles they deserve. “I find it fulfilling when I can see my patients’ beautiful smiles and how they can finally appreciate the joy of eating with a healthy set of teeth. However, what I love most about my job is the ability to provide a stress-free and comfortable experience at the dentist’s office, particularly for children, through sedation and general anesthesia.”</p>
    </div>
    <p class="bio-signature">Dr. Rowan Elke Marlon Quade, DDS</p>
    <div class="bio-photo" role="img" aria-label="Photo of a smiling woman reclining in a blue dental chair"></div>
  </section>

  <section class="panel panel--contact">
    <svg class="panel-bg" width="370" height="740" viewBox="0 0 370 740" aria-hidden="true">
      <path d="M370,0 C368,140 330,330 210,405 C120,425 40,440 0,470 L0,740 L370,740 Z" fill="var(--blue)"/>
      <path d="M370,0 C368,140 330,330 210,405 C120,425 40,440 0,470" fill="none" stroke="var(--orange)" stroke-width="14"/>
    </svg>
    <div class="brand-row">
      <span class="brand-dot"></span>
      <span class="brand-name">CALM CHAIR HUB</span>
    </div>
    <div class="portrait" role="img" aria-label="Portrait of the dentist in navy scrubs with a stethoscope"></div>
    <h2 class="contact-title">Contact Us !</h2>
    <div class="contact-icons">
      <span class="contact-icon"><svg width="18" height="18" viewBox="0 0 24 24"><path d="M12 2a7 7 0 0 0-7 7c0 5 7 13 7 13s7-8 7-13a7 7 0 0 0-7-7zm0 9.5A2.5 2.5 0 1 1 12 6.5a2.5 2.5 0 0 1 0 5z" fill="#fff"/></svg></span>
      <span class="contact-icon"><svg width="18" height="18" viewBox="0 0 24 24"><path d="M6.6 10.8a15 15 0 0 0 6.6 6.6l2.2-2.2a1 1 0 0 1 1-.25 11.4 11.4 0 0 0 3.6.6 1 1 0 0 1 1 1V20a1 1 0 0 1-1 1A17 17 0 0 1 3 4a1 1 0 0 1 1-1h3.5a1 1 0 0 1 1 1c0 1.25.2 2.45.6 3.6a1 1 0 0 1-.25 1z" fill="#fff"/></svg></span>
      <span class="contact-icon"><svg width="18" height="18" viewBox="0 0 24 24"><rect x="3" y="6" width="18" height="12" rx="1.5" fill="none" stroke="#fff" stroke-width="2"/><path d="M3.5 7l8.5 6 8.5-6" fill="none" stroke="#fff" stroke-width="2"/></svg></span>
    </div>
    <div class="contact-details">
      <p>48 Linden Harbor Avenue, Suite 210<br>Brookvale, Varnland 40219-0000</p>
      <p>1-555-014-2280<br>(555) 014-7731</p>
      <p>www.calmlearning.example</p>
    </div>
    <div class="url-pill">
      <svg width="22" height="22" viewBox="0 0 24 24"><g fill="none" stroke="#fff" stroke-width="1.6"><circle cx="12" cy="12" r="9"/><ellipse cx="12" cy="12" rx="4" ry="9"/><path d="M3 12h18M5 7h14M5 17h14"/></g></svg>
      www.calmchairhub.example
    </div>
  </section>

  <section class="panel panel--cover">
    <svg class="cover-photo" width="370" height="740" viewBox="0 0 370 740">
      <defs>
        <linearGradient id="coupleTones" x1="0" y1="0" x2="0.4" y2="1">
          <stop offset="0" stop-color="#cfe3f2"/>
          <stop offset="0.45" stop-color="#e6cbb4"/>
          <stop offset="1" stop-color="#f2f2f2"/>
        </linearGradient>
      </defs>
      <polygon points="370,170 370,222 26,740 0,740 0,705" fill="var(--orange)"/>
      <polygon points="370,222 370,740 26,740" fill="url(#coupleTones)" role="img" aria-label="Photo of a smiling young couple embracing outdoors"/>
    </svg>
    <div class="cover-brand">
      <span class="brand-dot"></span>
      <span class="brand-name">CALM CHAIR HUB</span>
    </div>
    <div class="url-pill">
      <svg width="22" height="22" viewBox="0 0 24 24"><g fill="none" stroke="#fff" stroke-width="1.6"><circle cx="12" cy="12" r="9"/><ellipse cx="12" cy="12" rx="4" ry="9"/><path d="M3 12h18M5 7h14M5 17h14"/></g></svg>
      www.calmchairhub.example
    </div>
    <p class="cover-tagline">Afraid of the dentist ?<br>You’ve come to the<br>right place.</p>
  </section>

</main>
</body>
</html>
```